Business Cards for a law firm

Business cards for our law firm. Use our silhoette logo and OAK HARBOR - check our website (www.oakharbor-legal.com)

Contact Information for Business Card

our silhouette logo, OAK HARBOR, 800-555-0147, Dorian Kestrup, dorian@oakharbor-legal.com

Requirements
Must have
• our silhouette logo, OAK HARBOR, 800-555-0147, Dorian Kestrup, dorian@oakharbor-legal.com

```html
<!DOCTYPE html>
<html lang="en">
<head>
<meta charset="utf-8">
<title>Oak Harbor – Business Cards</title>
<link href="https://fonts.googleapis.com/css2?family=Play:wght@400;700&family=Arimo:wght@400&display=swap" rel="stylesheet">
<style>
  :root {
    --navy: #1b316a;
    --white: #ffffff;
    --orange: #f7a823;
    --page: #ffffff;
    --edge: #e3e5ea;
  }
  * { margin: 0; padding: 0; box-sizing: border-box; }
  html, body {
    width: 1084px; height: 1200px; overflow: hidden;
    background: var(--page);
  }
  .card {
    position: absolute;
    left: 162px;
    width: 760px;
    height: 437px;
    overflow: hidden;
  }
  .card--front {
    top: 134px;
    background: var(--navy);
  }
  .card--back {
    top: 664px;
    background: var(--white);
    border: 1px solid var(--edge);
  }

  /* Front */
  .brand {
    position: absolute;
    left: 0; right: 0; top: 0; bottom: 0;
    display: flex; align-items: center; justify-content: center;
    gap: 20px;
  }
  .brand__mark {
    width: 34px; height: 34px;
    background: var(--white);
  }
  .brand__name {
    font-family: "Play", sans-serif;
    font-weight: 700;
    font-size: 50px;
    letter-spacing: 4px;
    color: var(--white);
  }

  /* Back */
  .figure {
    position: absolute;
    background: var(--navy);
    border-radius: 40px 40px 4px 4px;
  }
  .figure--left { left: 86px; top: 95px; width: 94px; height: 276px; }
  .figure--right { left: 601px; top: 111px; width: 89px; height: 260px; }

  .contact {
    position: absolute;
    left: 221px; top: 112px;
    color: var(--navy);
  }
  .contact__name {
    font-family: "Play", sans-serif;
    font-weight: 400;
    font-size: 42px;
    line-height: 1;
    margin-bottom: 22px;
  }
  .contact__list { list-style: none; }
  .contact__item {
    display: flex; align-items: center;
    height: 30px;
    margin-bottom: 17px;
    font-family: "Arimo", sans-serif;
    font-size: 22px;
  }
  .contact__icon {
    width: 30px; height: 30px;
    background: var(--orange);
    border-radius: 2px;
    display: flex; align-items: center; justify-content: center;
    margin-right: 16px;
    flex-shrink: 0;
  }
  .contact__icon svg { width: 18px; height: 18px; }

  .card__band {
    position: absolute;
    left: 0; right: 0; bottom: 0;
    height: 66px;
    background: var(--navy);
  }
</style>
</head>
<body>

<section class="card card--front">
  <div class="brand">
    <span class="brand__mark"></span>
    <span class="brand__name">OAK HARBOR</span>
  </div>
</section>

<section class="card card--back">
  <div class="figure figure--left" role="img" aria-label="Silhouette of a standing attorney in a suit"></div>
  <div class="figure figure--right" role="img" aria-label="Silhouette of a second standing attorney in a suit"></div>

  <div class="contact">
    <h1 class="contact__name">Dorian Kestrup</h1>
    <ul class="contact__list">
      <li class="contact__item">
        <span class="contact__icon">
          <svg viewBox="0 0 24 24" fill="none" stroke="#fff" stroke-width="2" stroke-linecap="round" stroke-linejoin="round"><path d="M6 3h3l1.5 4.5-2 1.5a11 11 0 0 0 6.5 6.5l1.5-2L21 15v3a2 2 0 0 1-2 2A16 16 0 0 1 4 5a2 2 0 0 1 2-2z"/></svg>
        </span>
        800-555-0147
      </li>
      <li class="contact__item">
        <span class="contact__icon">
          <svg viewBox="0 0 24 24" fill="none" stroke="#fff" stroke-width="1.6"><circle cx="12" cy="12" r="9"/><ellipse cx="12" cy="12" rx="4" ry="9"/><path d="M3 12h18M5 7h14M5 17h14"/></svg>
        </span>
        www.oakharbor-legal.com
      </li>
      <li class="contact__item">
        <span class="contact__icon">
          <svg viewBox="0 0 24 24" fill="none" stroke="#fff" stroke-width="1.8" stroke-linejoin="round"><rect x="3" y="6" width="18" height="12"/><path d="M3 6l9 7 9-7M3 18l7-6M21 18l-7-6"/></svg>
        </span>
        dorian@oakharbor-legal.com
      </li>
    </ul>
  </div>

  <div class="card__band"></div>
</section>

</body>
</html>
```